Corvantis websites redesign

Www.cor-vantis.com needs to be redesigned along with updations. The incremental material will be provided for the updations. We are looking for complete redesign of the pages with the new content. The complete write up will be provided soon

Target Market(s)

Global

Coding

Coded - Design and coding required

Number of Pages Required

5+ page

Requirements
Must have
• A clean and slick design for the Consulting.
Should not have
• Too many pictures which reduces the speed of the site

```html
<!DOCTYPE html>
<html lang="en">
<head>
<meta charset="utf-8">
<title>Corvantis Consultancy</title>
<link rel="stylesheet" href="https://fonts.googleapis.com/css2?family=Lato:wght@400;700&family=Raleway:wght@500;600;700&display=swap">
<style>
:root{
  --navy:#24324f;
  --maroon:#5e1e22;
  --maroon-btn:#6a2326;
  --sky:#39a9d4;
  --ink:#141414;
  --paper:#f3f3f3;
  --paper-2:#fafafa;
  --white:#ffffff;
  --text:#3c3c3c;
}
*{margin:0;padding:0;box-sizing:border-box}
html,body{width:717px;height:1200px;overflow:hidden;background:var(--white)}
body{font-family:"Lato",Arial,sans-serif;color:var(--text);position:relative}
.abs{position:absolute}

/* header */
.site-nav{position:absolute;left:0;top:0;width:717px;height:32px;background:rgba(0,0,0,.45);z-index:3}
.nav-link{position:absolute;top:11px;font:700 7px "Lato",sans-serif;color:var(--white);letter-spacing:.2px;text-transform:uppercase}
.nav-sep{position:absolute;top:10px;width:1px;height:9px;background:var(--white)}
.brand{position:absolute;left:256px;top:0;width:205px;height:68px;background:#f1f1f1;z-index:4;display:flex;align-items:center;justify-content:center;gap:8px}
.brand-mark{width:22px;height:22px;border-radius:50%;background:var(--navy)}
.brand-name{font:400 22px "Lato",sans-serif;color:var(--navy)}

/* hero */
.hero{position:absolute;left:0;top:0;width:717px;height:378px;overflow:hidden}
.hero-photo{position:absolute;inset:0;background:linear-gradient(135deg,#4a4a44 0%,#2e3430 40%,#3d3b36 70%,#26282a 100%)}
.hero-art{position:absolute;inset:0}
.hero-title{position:absolute;left:0;width:717px;top:124px;text-align:center;font:700 19.5px "Lato",sans-serif;color:var(--white);letter-spacing:.2px}
.hero-text{position:absolute;left:170px;width:377px;top:165px;text-align:center;font:700 7.6px/13.4px "Lato",sans-serif;color:var(--white)}
.btn{position:absolute;display:flex;align-items:center;justify-content:center;font:700 8px "Lato",sans-serif;color:var(--white);background:var(--maroon-btn);text-transform:uppercase}
.hero-btn{left:309px;top:215px;width:90px;height:21px;border:1px solid #d8d8d8}
.range{position:absolute;width:66px;height:66px;border-radius:50%;border:1px solid #d9d9d9;display:flex;align-items:center;justify-content:center;font:400 11px "Lato",sans-serif;color:var(--white)}
.dots{position:absolute;display:flex;gap:4px}
.dot{width:7px;height:7px;border-radius:50%;border:1px solid #cfcfcf}
.dot.on{background:var(--maroon);border-color:var(--maroon)}

/* welcome */
.welcome{position:absolute;left:0;top:378px;width:717px;height:178px;background:var(--paper)}
.section-title{font-family:"Raleway",sans-serif;font-weight:700}
.welcome-title{position:absolute;top:28px;width:717px;text-align:center;font-size:21px;color:var(--navy)}
.accent{color:var(--maroon)}
.welcome-text{position:absolute;left:76px;width:565px;top:69px;text-align:center;font:400 7.4px/14px "Lato",sans-serif;color:#555}
.welcome-btn{left:321px;top:124px;width:75px;height:21px}

/* consultancy */
.consultancy{position:absolute;left:0;top:556px;width:717px;height:366px;overflow:hidden}
.consult-photo{position:absolute;inset:0;background:linear-gradient(120deg,#232628 0%,#14171a 35%,#2b2b2a 65%,#1b1c1e 100%)}
.consult-title{position:absolute;top:29px;left:0;width:675px;text-align:center;font-size:20px;color:var(--white)}
.service-visual{position:absolute;width:86px;height:86px;border-radius:10px;transform:rotate(45deg);background:linear-gradient(135deg,#f4f4f4,#c9ced4)}
.service-name{position:absolute;font:700 16px "Lato",sans-serif;color:var(--sky);line-height:18px}
.service-sub{display:block;font:400 12.5px "Lato",sans-serif;color:var(--white);line-height:15px}
.service-more{position:absolute}

/* testimonials */
.testimonials{position:absolute;left:0;top:922px;width:717px;height:230px;background:var(--paper-2)}
.quote-badge{position:absolute;left:336px;top:25px;width:44px;height:44px;border-radius:50%;border:1px solid #8a8a8a;display:flex;align-items:center;justify-content:center}
.testi-title{position:absolute;top:72px;width:730px;text-align:center;font-size:16px;font-weight:500;color:var(--navy)}
.testi-rule{position:absolute;left:357px;top:96px;width:1px;height:33px;background:#555}
.testi-text{position:absolute;left:80px;width:560px;top:134px;text-align:center;font:400 7.4px/16px "Lato",sans-serif;color:#444}
.testi-author{position:absolute;top:173px;left:0;width:709px;text-align:center;font:400 10px "Lato",sans-serif;color:var(--maroon)}
.author-rule{position:absolute;top:180px;height:1px;width:56px;background:#555}
.testi-dots .dot{border-color:#555}

/* footer */
.site-footer{position:absolute;left:0;top:1152px;width:717px;height:48px;background:var(--ink)}
.copyright{position:absolute;left:32px;top:19px;font:400 7.4px "Lato",sans-serif;color:var(--white)}
.social{position:absolute;top:24px;display:flex;gap:14px;left:584px}
.social-dot{width:8px;height:8px;border-radius:50%;background:#8a8a8a}
</style>
</head>
<body>

<header>
  <nav class="site-nav">
    <span class="nav-link" style="left:39px">Home</span>
    <span class="nav-sep" style="left:77px"></span>
    <span class="nav-link" style="left:99px">Founder</span>
    <span class="nav-sep" style="left:150px"></span>
    <span class="nav-link" style="left:170px">Consultancy</span>
    <span class="nav-link" style="left:490px">System</span>
    <span class="nav-sep" style="left:536px"></span>
    <span class="nav-link" style="left:556px">Case Studies</span>
    <span class="nav-sep" style="left:622px"></span>
    <span class="nav-link" style="left:642px">Contact Us</span>
  </nav>
  <div class="brand"><span class="brand-mark"></span><span class="brand-name">Corvantis</span></div>
</header>

<section class="hero">
  <div class="hero-photo" role="img" aria-label="Team of consultants working together around a table with a tablet"></div>
  <svg class="hero-art" width="717" height="378" viewBox="0 0 717 378">
    <rect width="717" height="378" fill="rgba(0,0,0,.25)"/>
    <polygon points="0,122 104,224 0,330" fill="rgba(255,255,255,.55)"/>
    <polygon points="717,122 601,224 717,330" fill="rgba(255,255,255,.55)"/>
    <polygon points="632,120 700,120 717,140 717,160" fill="rgba(255,255,255,.25)"/>
    <line x1="172" y1="224" x2="262" y2="224" stroke="#fff" stroke-width="1.5"/>
    <line x1="453" y1="224" x2="533" y2="224" stroke="#fff" stroke-width="1.5"/>
    <polygon points="104,156 172,224 104,302 36,224" fill="#2b3a5c" stroke="#fff" stroke-width="1.5"/>
    <polygon points="601,146 669,224 601,302 533,224" fill="#6b2327" stroke="#fff" stroke-width="1.5"/>
    <circle cx="99" cy="226" r="11" fill="#d4d4d4"/>
    <polyline points="101,221 96,226 101,231" fill="none" stroke="#444" stroke-width="1.6"/>
    <circle cx="597" cy="222" r="11" fill="#d4d4d4"/>
    <polyline points="595,217 600,222 595,227" fill="none" stroke="#444" stroke-width="1.6"/>
  </svg>
  <h1 class="hero-title">CORVANTIS CONSULTANCY LIMITED CAPITALIZES</h1>
  <p class="hero-text">Lorem ipsum dolor sit amet, consectetur adipiscing elit, sed do eiusmod tempor incididunt ut labore et dolore magna aliqua. Ut enim ad minim veniam, quis nostrud exercitation ullamco laboris nisi ut aliquip ex ea commodo consequat. Duis aute irure dolor</p>
  <a class="btn hero-btn">Read More</a>
  <div class="range" style="left:207px;top:259px;background:#6a2326">0 - 250</div>
  <div class="range" style="left:289px;top:259px;background:#253556">250 - 500</div>
  <div class="range" style="left:369px;top:262px;background:var(--sky)">500 - 1000</div>
  <div class="range" style="left:452px;top:259px;background:#111">&gt; 1000</div>
  <div class="dots" style="left:347px;top:358px"><span class="dot"></span><span class="dot"></span><span class="dot on"></span><span class="dot"></span><span class="dot"></span></div>
</section>

<section class="welcome">
  <h2 class="section-title welcome-title">Welcome to <span class="accent">Corvantis</span></h2>
  <p class="welcome-text">Lorem ipsum dolor sit amet, consectetur adipiscing elit, sed do eiusmod tempor incididunt ut labore et dolore magna aliqua. Ut enim ad minim veniam, quis nostrud exercitation ullamco laboris nisi ut aliquip ex ea commodo consequat. Duis aute irure dolor in reprehenderit in voluptate velit esse cillum dolore eu fugiat nulla pariatur. Excepteur sint occaecat cupidatat non proident, sunt in culpa qui officia deserunt mollit anim id est laborum.</p>
  <a class="btn welcome-btn">Read More</a>
</section>

<section class="consultancy">
  <div class="consult-photo" role="img" aria-label="Business people reviewing documents at a laptop in an office"></div>
  <h2 class="section-title consult-title">Consultancy</h2>
  <svg class="abs" style="left:0;top:0" width="717" height="366" viewBox="0 0 717 366">
    <line x1="334" y1="70" x2="334" y2="294" stroke="#8a8a8a" stroke-width="1"/>
    <line x1="230" y1="140" x2="334" y2="140" stroke="#8a8a8a" stroke-width="1"/>
    <line x1="334" y1="222" x2="440" y2="222" stroke="#8a8a8a" stroke-width="1"/>
    <polygon points="334,134 340,140 334,146 328,140" fill="var(--sky)"/>
    <polygon points="334,216 340,222 334,228 328,222" fill="var(--sky)"/>
  </svg>
  <div class="service-visual" role="img" aria-label="Hand drawing a rising bar chart" style="left:139px;top:97px"></div>
  <div class="service-visual" role="img" aria-label="Hands pointing at financial charts on paper" style="left:446px;top:183px"></div>
  <div class="service-name" style="left:428px;top:122px;text-align:right">PLAIN VANILLA<span class="service-sub">Financing Solutions</span></div>
  <svg class="service-more" style="left:557px;top:134px" width="12" height="12" viewBox="0 0 12 12"><circle cx="6" cy="6" r="6" fill="#fff"/><polyline points="5,3 8,6 5,9" fill="none" stroke="#111" stroke-width="1.6"/></svg>
  <div class="service-name" style="left:127px;top:207px">STRUCTURED<span class="service-sub">Financing Solutions</span></div>
  <svg class="service-more" style="left:245px;top:216px" width="12" height="12" viewBox="0 0 12 12"><circle cx="6" cy="6" r="6" fill="#fff"/><polyline points="5,3 8,6 5,9" fill="none" stroke="#111" stroke-width="1.6"/></svg>
</section>

<section class="testimonials">
  <div class="quote-badge">
    <svg width="28" height="24" viewBox="0 0 28 24"><path d="M14 1C7 1 1 5 1 10c0 3 2 5.5 5 7l-2 6 7-4.5c1 .2 2 .3 3 .3 7 0 13-4 13-9S21 1 14 1z" fill="var(--maroon)"/><text x="14" y="15" text-anchor="middle" font-family="Lato,sans-serif" font-weight="700" font-size="11" fill="#fff">"</text></svg>
  </div>
  <h2 class="section-title testi-title">CLIENT <span class="accent">TESTIMONIALS</span></h2>
  <span class="testi-rule"></span>
  <p class="testi-text">Lorem ipsum dolor sit amet, consectetur adipiscing elit, sed do eiusmod tempor incididunt ut labore et dolore magna aliqua. Ut enim ad minim veniam, quis nostrud exercitation ullamco laboris nisi ut aliquip ex ea commodo consequat.</p>
  <span class="author-rule" style="left:263px"></span>
  <p class="testi-author">Daniel Reyes</p>
  <span class="author-rule" style="left:397px"></span>
  <div class="dots testi-dots" style="left:342px;top:201px"><span class="dot"></span><span class="dot" style="background:#555"></span><span class="dot"></span></div>
</section>

<footer class="site-footer">
  <p class="copyright">All Rights Reserved. Copyrights @company Name. 2016</p>
  <div class="social"><span class="social-dot"></span><span class="social-dot"></span><span class="social-dot"></span><span class="social-dot"></span><span class="social-dot"></span></div>
</footer>

</body>
</html>
```